Podcast cover art (not a logo)

I’m launching an audio-only podcast for parents of neurodivergent children. The podcast is meant to feel like a calm, trusted professional voice — not a brand or a performance.

Style direction:
--Clean and minimal
--Calm and grounded
--Professional, not playful
--Nothing flashy, loud, or busy
--No cartoon imagery

Content on the cover:
--Podcast title: Under the Quiet Surface
--Subtitle or tagline: Supporting Neurodivergent Kids with Science, Not Shame (or Understanding Neurodivergent Kids)
--No episode numbers, no dates

Design preferences:
--Text-forward design
--Neutral or soft colors (muted blues, grays, off-whites)
--High contrast for readability at small sizes
--Simple, timeless font

What I do NOT want:
--A logo or branding system
--Illustrations of children or families
--Bright colors or playful graphics
--Trendy fonts or visual effects

Technical requirements:
--Square image
--3000 × 3000 pixels
--RGB color mode
--JPEG or PNG
--File size under 500 KB

Deliverables:
--Final cover art file
--Optional: one or two alternate background color versions

```html
<!DOCTYPE html>
<html lang="en">
<head>
<meta charset="utf-8">
<title>Under the Quiet Surface — Podcast Cover</title>
<link rel="stylesheet" href="https://fonts.googleapis.com/css2?family=Outfit:wght@400;700&display=swap">
<style>
  :root {
    --sky: #00aee4;
    --sunlight: #f2da4b;
    --paper: #ffffff;
  }
  html, body {
    margin: 0;
    padding: 0;
    overflow: hidden;
    background: var(--sky);
  }
  .cover {
    display: block;
    width: 1200px;
    height: 1200px;
  }
  .cover-background { fill: var(--sky); }
  .accent-rule { fill: var(--sunlight); }
  .title {
    font-family: "Outfit", sans-serif;
    font-weight: 700;
    font-size: 188px;
    letter-spacing: -2px;
    filter: drop-shadow(0 4px 6px rgba(0, 60, 90, 0.18));
  }
  .title-light { fill: var(--paper); }
  .title-accent { fill: var(--sunlight); }
  .tagline {
    font-family: "Outfit", sans-serif;
    font-weight: 400;
    font-size: 52px;
    fill: var(--paper);
  }
</style>
</head>
<body>
<svg class="cover" viewBox="0 0 1200 1200" xmlns="http://www.w3.org/2000/svg" role="img" aria-label="Under the Quiet Surface: Supporting Neurodivergent Kids with Science, Not Shame">
  <rect class="cover-background" x="0" y="0" width="1200" height="1200"/>

  <rect class="accent-rule" x="1078" y="0" width="25" height="204"/>
  <rect class="accent-rule" x="92" y="1008" width="944" height="26"/>
  <rect class="accent-rule" x="92" y="1008" width="25" height="192"/>

  <text class="title title-light" x="162" y="404">Under</text>
  <text class="title title-light" x="162" y="582">the Quiet</text>
  <text class="title title-accent" x="162" y="776">Surface</text>

  <text class="tagline" x="162" y="870">Supporting Neurodivergent Kids</text>
  <text class="tagline" x="162" y="936">with Science, Not Shame</text>
</svg>
</body>
</html>
```